RMT Concreting and Excavation website design

We need a new webpage for our concreting business.

It just have the following pages
Home
Services
Galley
Online quote
FAQ
Contact

Examples are:
https://www.brookvaleworksbuild.example

Industry/Entity Type

Concreting

Font styles to use
Serif
Sans Serif

Colors
0054AA
0677BA
7BADD7
CADEEF
E8F1F8
0094D4
00A9DD
6FCCEA
C7EBF8
E9F6FB
59FF00
82FF00
B8FF75
E3FFCB
F4FFEA

Requirements
Should not have
• No shopping cart

```html
<!DOCTYPE html>
<html lang="en">
<head>
<meta charset="utf-8">
<title>RMT Concreting &amp; Excavation</title>
<link href="https://fonts.googleapis.com/css2?family=Raleway:wght@300;400&family=Roboto:wght@400;500;700&display=swap" rel="stylesheet">
<style>
:root{
  --green:#7dc142;
  --green-dark:#5e9a2c;
  --ink:#2b2b2b;
  --text:#666;
  --grey-bg:#f3f3f3;
  --white:#fff;
  --dark-btn:#333;
  --footer-top:#4a3d33;
  --footer-bottom:#2e2620;
}
*{margin:0;padding:0;box-sizing:border-box}
html,body{width:1200px;height:3980px;overflow:hidden}
body{position:relative;font-family:'Roboto',sans-serif;color:var(--text);background:var(--white)}
.abs{position:absolute}
.heading{font-family:'Raleway',sans-serif;font-weight:400;color:var(--ink);font-size:36px;letter-spacing:1px;text-transform:uppercase}
.heading span{color:var(--green)}
.btn{position:absolute;display:flex;align-items:center;justify-content:center;gap:10px;background:var(--green);color:var(--white);font-size:15px;font-weight:500;text-transform:uppercase;border-radius:2px}
.btn svg{width:15px;height:15px}
.body-copy{font-size:14px;line-height:25.7px;text-align:justify;color:#777}
.photo{position:absolute}

/* header */
.header{top:0;left:0;width:1200px;height:85px;background:var(--white)}
.icon-circle{position:absolute;width:34px;height:34px;border-radius:50%;background:var(--green);display:flex;align-items:center;justify-content:center}
.icon-circle svg{width:16px;height:16px}
.header .addr{left:164px;top:23px;font-size:14px;line-height:20px;color:#777}
.brand{left:0;width:1200px;top:22px;text-align:center;font-family:'Roboto',sans-serif;font-weight:700;font-size:22px;color:var(--ink);letter-spacing:1px}
.brand-sub{left:0;width:1200px;top:52px;text-align:center;font-weight:700;font-size:11px;letter-spacing:2px;color:var(--ink);text-transform:uppercase}
.call-label{left:925px;top:20px;font-size:14px;color:var(--ink)}
.call-num{left:925px;top:39px;font-size:21px;font-weight:700;color:var(--green)}

.nav{top:85px;left:0;width:1200px;height:45px;background:var(--green);display:flex;justify-content:center;align-items:center;gap:29px}
.nav a{color:var(--white);font-size:14px;font-weight:700;text-decoration:none;text-transform:uppercase}
.nav a.gap{margin-left:14px}

/* hero */
.hero{top:130px;left:0;width:1200px;height:557px;background:linear-gradient(180deg,#6b6a5c 0%,#8a7d68 40%,#9a9184 60%,#6f5a45 100%)}
.hero-title{left:0;width:1200px;top:105px;text-align:center;font-family:'Raleway',sans-serif;font-weight:300;font-size:55px;line-height:60px;color:var(--white)}
.hero-sub{left:0;width:1200px;top:243px;text-align:center;font-size:16px;line-height:24px;color:var(--white)}
.dots{left:572px;top:497px;display:flex;gap:4px}
.dots i{width:8px;height:8px;border-radius:50%;background:var(--white);display:block}
.dots i.on{background:var(--green)}

/* about */
.about-frame{left:111px;top:794px;width:393px;height:341px;border:8px solid var(--green);background:var(--white);padding:6px}
.about-frame .photo{inset:6px;background:linear-gradient(160deg,#9db5c9 0%,#c2a77f 40%,#a08565 100%)}
.about-video{left:352px;top:1011px;width:201px;height:173px;background:linear-gradient(160deg,#c9d1d8 0%,#8d8c80 55%,#5a4f40 100%)}
.play{position:absolute;left:76px;top:62px;width:48px;height:48px;border-radius:50%;background:var(--green);display:flex;align-items:center;justify-content:center}

/* services */
.services{top:1288px;left:0;width:1200px;height:1212px;background:var(--grey-bg)}
.svc-icon{position:absolute;width:78px;height:78px;border-radius:50%;background:var(--green);border:6px solid var(--white);display:flex;align-items:center;justify-content:center}
.svc-icon svg{width:34px;height:34px}

/* gallery */
.gal{position:absolute;background:linear-gradient(170deg,#a9bccb 0%,#bfbfb8 45%,#8c8a85 100%)}

/* cta */
.cta{top:3385px;left:0;width:1200px;height:215px;background:linear-gradient(180deg,#8cc63f 0%,#7bb23c 55%,#5c6a3a 85%,#4a3d33 100%)}
.cta-title{left:111px;top:48px;font-family:'Raleway',sans-serif;font-weight:300;font-size:55px;color:var(--white)}
.cta-text{left:111px;top:128px;width:990px;font-size:15px;line-height:25px;color:var(--white)}
.btn.dark{background:var(--dark-btn);font-size:14px}

/* footer */
.footer{top:3600px;left:0;width:1200px;height:380px;background:linear-gradient(180deg,var(--footer-top) 0%,var(--footer-bottom) 100%);color:var(--white)}
.f-head{position:absolute;top:76px;font-size:15px;font-weight:700;text-decoration:underline;text-transform:uppercase}
.f-list{position:absolute;top:103px;list-style:none;font-size:14px}
.f-list li{height:34px;display:flex;align-items:center;gap:12px}
.f-list li::before{content:'»';font-size:15px}
.hours li span{display:inline-block}
.contact-row{position:absolute;left:508px;display:flex;gap:18px;font-size:13px;line-height:20px;width:260px}
.contact-row .icon-circle{position:relative;flex:none;width:30px;height:30px;background:var(--white)}
.f-rule{left:111px;top:3906px;width:978px;height:1px;background:rgba(255,255,255,.45)}
.copy{left:0;width:1200px;top:3928px;text-align:center;font-size:14px;color:var(--white)}
</style>
</head>
<body>

<header class="abs header">
  <div class="icon-circle" style="left:107px;top:25px">
    <svg viewBox="0 0 24 24"><path fill="#fff" d="M12 2a7 7 0 0 0-7 7c0 5 7 13 7 13s7-8 7-13a7 7 0 0 0-7-7zm0 9.5A2.5 2.5 0 1 1 12 6.5a2.5 2.5 0 0 1 0 5z"/></svg>
  </div>
  <div class="abs addr">Kellerton Park, ACT, Australia 2999<br>GENERAL</div>
  <div class="abs brand">RMT</div>
  <div class="abs brand-sub">Concreting &amp; Excavation</div>
  <div class="icon-circle" style="left:868px;top:25px">
    <svg viewBox="0 0 24 24"><path fill="#fff" d="M6.6 10.8a15 15 0 0 0 6.6 6.6l2.2-2.2a1 1 0 0 1 1-.25 11.4 11.4 0 0 0 3.6.57 1 1 0 0 1 1 1V20a1 1 0 0 1-1 1A17 17 0 0 1 3 4a1 1 0 0 1 1-1h3.5a1 1 0 0 1 1 1c0 1.25.2 2.45.57 3.57a1 1 0 0 1-.25 1z"/></svg>
  </div>
  <div class="abs call-label">Call Us Now</div>
  <div class="abs call-num">+61 400 123 456</div>
</header>

<nav class="abs nav">
  <a>Home</a><a>Concrete Services</a><a>Concretes</a><a>Projects</a><a>Reviews</a><a>About</a><a class="gap">Request Free Estimate</a><a>Contact</a>
</nav>

<section class="abs hero" role="img" aria-label="Photo of a freshly poured concrete slab on a building site">
  <h1 class="abs hero-title">RMT CONCRETING &amp;<br>EXCAVATION</h1>
  <p class="abs hero-sub">Sed ut perspiciatis unde omnis iste natus error sit voluptatem accusantium doloremque laudantium,<br>totam rem aperiam, eaque ipsa quae ab illo inventore veritatis et quasi architecto</p>
  <div class="btn" style="left:523px;top:318px;width:155px;height:45px">Get Started
    <svg viewBox="0 0 16 16"><circle cx="8" cy="8" r="8" fill="#fff"/><path d="M6.5 4.5 10 8l-3.5 3.5" stroke="#7dc142" stroke-width="2" fill="none"/></svg></div>
  <div class="abs dots"><i></i><i></i><i class="on"></i><i></i><i></i></div>
</section>

<!-- about -->
<div class="abs about-frame"><div class="photo" role="img" aria-label="Photo of road construction with excavators and trucks"></div></div>
<div class="abs about-video" role="img" aria-label="Video thumbnail of an excavator at work">
  <div class="play"><svg width="20" height="20" viewBox="0 0 20 20"><path d="M6 3l11 7-11 7z" fill="#fff"/></svg></div>
</div>
<h2 class="abs heading" style="left:642px;top:807px">About <span>Us</span></h2>
<p class="abs body-copy" style="left:642px;top:864px;width:441px">At vero eos et accusamus et iusto odio dignissimos ducimus qui blanditiis praesentium voluptatum deleniti atque corrupti quos dolores et quas molestias excepturi sint occaecati cupiditate non provident, similique sunt in culpa qui officia deserunt mollitia animi, id est laborum et dolorum fuga. Et harum quidem rerum facilis est et expedita distinctio. Nam libero tempore, cum soluta nobis est eligendi optio cumque nihil impedit quo minus id quod maxime placeat facere possimus, omnis voluptas assumenda est, omnis dolor repellendus. Temporibus autem quibusdam</p>
<div class="btn" style="left:642px;top:1120px;width:155px;height:46px">Learn More
  <svg viewBox="0 0 16 16"><circle cx="8" cy="8" r="8" fill="#fff"/><path d="M6.5 4.5 10 8l-3.5 3.5" stroke="#7dc142" stroke-width="2" fill="none"/></svg></div>

<!-- services -->
<section class="abs services">
  <h2 class="abs heading" style="left:0;width:1200px;text-align:center;top:78px">Our <span>Services</span></h2>
  <p class="abs" style="left:0;width:1200px;top:137px;text-align:center;font-size:17px;line-height:26px;color:#666">Sed ut perspiciatis unde omnis iste natus error sit voluptatem accusantium doloremque<br>laudantium, totam rem aperiam, eaque ipsa quae ab illo inventore veritatis et quasi architecto beatae</p>

  <h3 class="abs heading" style="left:111px;top:291px;font-size:31px">Concreting</h3>
  <p class="abs body-copy" style="left:111px;top:342px;width:393px">At vero eos et accusamus et iusto odio dignissimos ducimus qui blanditiis praesentium voluptatum deleniti atque corrupti quos dolores et quas molestias excepturi sint occaecati cupiditate non provident, similique sunt in culpa qui officia deserunt mollitia animi, id est laborum et dolorum fuga. Et harum quidem rerum facilis est et expedita distinctio. Nam libero tempore, cum soluta nobis est eligendi optio cumque nihil impedit quo minus id quod</p>
  <div class="btn" style="left:111px;top:566px;width:155px;height:46px">Learn More
    <svg viewBox="0 0 16 16"><circle cx="8" cy="8" r="8" fill="#fff"/><path d="M6.5 4.5 10 8l-3.5 3.5" stroke="#7dc142" stroke-width="2" fill="none"/></svg></div>
  <div class="photo" style="left:598px;top:233px;width:491px;height:445px;background:linear-gradient(170deg,#8aa6bf 0%,#6f7f5a 30%,#4d5052 60%,#c6ad86 100%)" role="img" aria-label="Photo of a new concrete path curving beside a garden"></div>
  <div class="svc-icon" style="left:559px;top:415px"><svg viewBox="0 0 24 24" fill="#fff"><rect x="3" y="8" width="12" height="8" rx="2"/><rect x="15" y="10" width="6" height="6"/><circle cx="6" cy="18" r="2"/><circle cx="17" cy="18" r="2"/></svg></div>

  <div class="photo" style="left:111px;top:679px;width:489px;height:445px;background:linear-gradient(180deg,#6e8aa8 0%,#d9a46a 40%,#c88b4e 65%,#6e5139 100%)" role="img" aria-label="Photo of an excavator digging at sunset"></div>
  <div class="svc-icon" style="left:559px;top:863px"><svg viewBox="0 0 24 24" fill="#fff"><rect x="3" y="13" width="10" height="5" rx="1"/><path d="M13 13l4-7 4 5h-3l-2-2-2 4z"/><rect x="3" y="19" width="10" height="2"/></svg></div>
  <h3 class="abs heading" style="left:693px;top:736px;font-size:31px">Excavation</h3>
  <p class="abs body-copy" style="left:693px;top:787px;width:393px">At vero eos et accusamus et iusto odio dignissimos ducimus qui blanditiis praesentium voluptatum deleniti atque corrupti quos dolores et quas molestias excepturi sint occaecati cupiditate non provident, similique sunt in culpa qui officia deserunt mollitia animi, id est laborum et dolorum fuga. Et harum quidem rerum facilis est et expedita distinctio. Nam libero tempore, cum soluta nobis est eligendi optio cumque nihil impedit quo minus id quod</p>
  <div class="btn" style="left:693px;top:1011px;width:155px;height:46px">Learn More
    <svg viewBox="0 0 16 16"><circle cx="8" cy="8" r="8" fill="#fff"/><path d="M6.5 4.5 10 8l-3.5 3.5" stroke="#7dc142" stroke-width="2" fill="none"/></svg></div>
</section>

<!-- gallery -->
<h2 class="abs heading" style="left:0;width:1200px;text-align:center;top:2568px">Our <span>Gallery</span></h2>
<div class="gal" style="left:111px;top:2648px;width:317px;height:310px" role="img" aria-label="Photo of a concrete crossing with traffic cones"></div>
<div class="gal" style="left:442px;top:2648px;width:316px;height:310px;background:linear-gradient(170deg,#b7c6d3 0%,#c9c7bf 40%,#a89b86 100%)" role="img" aria-label="Photo of a newly laid footpath"></div>
<div class="gal" style="left:772px;top:2648px;width:317px;height:310px;background:linear-gradient(170deg,#8fb0cf 0%,#6e8456 40%,#9b9a94 100%)" role="img" aria-label="Photo of a curved concrete path with safety fencing"></div>
<div class="gal" style="left:111px;top:2974px;width:482px;height:309px;background:linear-gradient(180deg,#6f6a5d 0%,#9a9a96 50%,#5e5a52 100%)" role="img" aria-label="Photo of a concrete driveway crossover"></div>
<div class="gal" style="left:605px;top:2974px;width:484px;height:309px;background:linear-gradient(170deg,#a9c0d4 0%,#778860 40%,#b8b5ac 100%)" role="img" aria-label="Photo of workers finishing a concrete footpath"></div>

<!-- cta -->
<section class="abs cta">
  <h2 class="abs cta-title">LOREM IPSUM DOLOR</h2>
  <div class="btn dark" style="left:800px;top:50px;width:222px;height:47px">Get A Online Quote
    <svg viewBox="0 0 16 16"><circle cx="8" cy="8" r="8" fill="#fff"/><path d="M6.5 4.5 10 8l-3.5 3.5" stroke="#333" stroke-width="2" fill="none"/></svg></div>
  <p class="abs cta-text">At vero eos et accusamus et iusto odio dignissimos ducimus qui blanditiis praesentium voluptatum deleniti atque corrupti quos dolores et quas molestias excepturi sint occaecati cupiditate non provident, similique sunt in culpa</p>
</section>

<!-- footer -->
<footer class="abs footer">
  <div class="f-head" style="left:111px">Quick Links</div>
  <ul class="f-list" style="left:111px"><li>Home</li><li>About Us</li><li>Services</li><li>Contact Us</li><li>Gallery</li></ul>
  <div class="f-head" style="left:309px">Other Links</div>
  <ul class="f-list" style="left:309px"><li>FAQ</li><li>Help Service</li><li>Terms Of Use</li><li>Privacy Policy</li><li>Our Videos</li></ul>
  <div class="f-head" style="left:508px">Contact Us</div>
  <div class="contact-row" style="top:106px">
    <div class="icon-circle"><svg viewBox="0 0 24 24"><path fill="#7dc142" d="M12 2a7 7 0 0 0-7 7c0 5 7 13 7 13s7-8 7-13a7 7 0 0 0-7-7zm0 9.5A2.5 2.5 0 1 1 12 6.5a2.5 2.5 0 0 1 0 5z"/></svg></div>
    <span>Kellerton Park, ACT, Australia<br>2999</span></div>
  <div class="contact-row" style="top:167px;align-items:center">
    <div class="icon-circle"><svg viewBox="0 0 24 24"><path fill="#7dc142" d="M6.6 10.8a15 15 0 0 0 6.6 6.6l2.2-2.2a1 1 0 0 1 1-.25 11.4 11.4 0 0 0 3.6.57 1 1 0 0 1 1 1V20a1 1 0 0 1-1 1A17 17 0 0 1 3 4a1 1 0 0 1 1-1h3.5a1 1 0 0 1 1 1c0 1.25.2 2.45.57 3.57a1 1 0 0 1-.25 1z"/></svg></div>
    <span>+61 400 123 456</span></div>
  <div class="contact-row" style="top:225px;align-items:center">
    <div class="icon-circle"><svg viewBox="0 0 24 24"><rect x="3" y="6" width="18" height="12" rx="1" fill="none" stroke="#7dc142" stroke-width="2"/><path d="M3 7l9 6 9-6" fill="none" stroke="#7dc142" stroke-width="2"/></svg></div>
    <span>info@rmtconcreting.example</span></div>
  <div class="f-head" style="left:835px">Hours of Operation</div>
  <ul class="f-list hours" style="left:835px;font-size:14px">
    <li style="height:30px"><span style="width:80px">Monday</span><span>:&nbsp;&nbsp; 07:00 - 17:00</span></li>
    <li style="height:30px"><span style="width:80px">Tuesday</span><span>:&nbsp;&nbsp; 07:00 - 17:00</span></li>
    <li style="height:30px"><span style="width:80px">Wednesday</span><span>:&nbsp;&nbsp; 07:00 - 17:00</span></li>
    <li style="height:30px"><span style="width:80px">Thursday</span><span>:&nbsp;&nbsp; 07:00 - 17:00</span></li>
    <li style="height:30px"><span style="width:80px">Friday</span><span>:&nbsp;&nbsp; 07:00 - 17:00</span></li>
    <li style="height:30px"><span style="width:80px">Saturday</span><span>:&nbsp;&nbsp; 08:00 - 12:00</span></li>
  </ul>
</footer>
<div class="abs f-rule"></div>
<div class="abs copy">© 2021 RMT Concreting. All Rights Reserved</div>

</body>
</html>
```